Home Remodeling company needs a business card design

we need a business card design for home remodeling company in hamilton county, indiana USA. we offers a wide range of construction services including whole house renovations, Design and Build Basements and Kitchen and Bathroom Remodeling . we would like to see designs for both site of business card that use the same color of the company logo and also including all information below :
1- Tarek Salim CEO / General Contractor
2- all company contacts Telephone numbers ( 1-888-VOLMI-15 ) ( 317-555-0192) email address ( info@volmihome.example) website ( www.volmihome.example ) and social media logos (Facebook- twitter- google plus )
3- company logo
4- licensed . insured . bonded

```html
<!DOCTYPE html>
<html lang="en">
<head>
<meta charset="utf-8">
<title>Volmi Home Remodeling – Business Card</title>
<link href="https://fonts.googleapis.com/css2?family=Arimo:wght@400;700&display=swap" rel="stylesheet">
<style>
  :root {
    --bg: #e9e7e4;
    --card-white: #ffffff;
    --card-grey: #f1f1f1;
    --brand-red: #c8313c;
    --band-salmon: #e5907f;
    --ink-dark: #48484b;
    --ink-mid: #6a6a6d;
    --line-red: #d9868b;
  }
  * { box-sizing: border-box; margin: 0; padding: 0; }
  html, body {
    width: 1200px; height: 1000px; overflow: hidden;
    background: var(--bg);
    font-family: "Arimo", Arial, sans-serif;
  }
  .card {
    position: absolute;
    width: 720px; height: 411px;
    left: 240px;
    overflow: hidden;
    box-shadow: 0 6px 18px rgba(0,0,0,.18);
  }
  .card-front { top: 62px; background: var(--card-white); }
  .card-back {
    top: 527px;
    background: radial-gradient(ellipse at 50% 50%, #ffffff 0%, var(--card-grey) 75%, #e4e4e4 100%);
  }
  .card-art { position: absolute; inset: 0; }

  /* Company name */
  .company { position: absolute; display: flex; align-items: center; white-space: nowrap; }
  .company-dot { background: var(--brand-red); flex: none; }
  .company-name { color: var(--ink-dark); font-weight: 700; line-height: 1; }

  .company-small { top: 44px; right: 40px; gap: 10px; }
  .company-small .company-dot { width: 12px; height: 12px; }
  .company-small .company-name { font-size: 24px; }

  .company-large { top: 182px; left: 0; right: 0; justify-content: center; gap: 16px; }
  .company-large .company-dot { width: 22px; height: 22px; }
  .company-large .company-name { font-size: 44px; }

  /* Front details */
  .person-name {
    position: absolute; left: 40px; top: 232px;
    font-size: 26px; font-weight: 700; color: #fff;
  }
  .person-role {
    position: absolute; left: 330px; top: 250px;
    font-size: 18px; color: #fff;
  }
  .contacts { position: absolute; left: 40px; bottom: 30px; display: flex; align-items: flex-end; gap: 26px; color: #fff; }
  .social { display: flex; gap: 8px; margin-bottom: 44px; }
  .social-icon { width: 28px; height: 28px; border-radius: 50%; background: #fff; display: flex; align-items: center; justify-content: center; }
  .contact-list { display: flex; flex-direction: column; gap: 12px; }
  .contact-row { display: flex; align-items: center; gap: 14px; font-size: 19px; line-height: 1.2; }
  .contact-row svg { flex: none; }

  /* Back details */
  .credentials {
    position: absolute; top: 26px; right: 40px;
    font-size: 17px; color: var(--ink-mid); letter-spacing: .5px;
  }
  .website {
    position: absolute; bottom: 24px; left: 40px;
    font-size: 16px; color: var(--ink-mid);
  }
</style>
</head>
<body>

<section class="card card-front" aria-label="Business card front">
  <svg class="card-art" viewBox="0 0 720 411" preserveAspectRatio="none" aria-hidden="true">
    <polygon points="0,228 720,108 720,178 0,298" fill="var(--band-salmon)"/>
    <polygon points="0,298 720,178 720,411 0,411" fill="var(--brand-red)"/>
  </svg>

  <div class="company company-small">
    <span class="company-dot"></span>
    <span class="company-name">Volmi Home Remodeling</span>
  </div>

  <p class="person-name">Tarek Salim</p>
  <p class="person-role">CEO / General Contractor</p>

  <div class="contacts">
    <div class="social" aria-label="Social media">
      <span class="social-icon">
        <svg width="16" height="16" viewBox="0 0 16 16" aria-hidden="true">
          <path d="M2 3h12v8H7l-3 3v-3H2z" fill="var(--brand-red)"/>
        </svg>
      </span>
      <span class="social-icon">
        <svg width="16" height="16" viewBox="0 0 16 16" aria-hidden="true">
          <circle cx="8" cy="8" r="6" fill="none" stroke="var(--brand-red)" stroke-width="1.6"/>
          <path d="M2 8h12M8 2c3 3 3 9 0 12M8 2c-3 3-3 9 0 12" fill="none" stroke="var(--brand-red)" stroke-width="1.3"/>
        </svg>
      </span>
      <span class="social-icon">
        <svg width="16" height="16" viewBox="0 0 16 16" aria-hidden="true">
          <path d="M3 8h9M8.5 4l4 4-4 4" fill="none" stroke="var(--brand-red)" stroke-width="2" stroke-linecap="round" stroke-linejoin="round"/>
        </svg>
      </span>
    </div>
    <div class="contact-list">
      <div class="contact-row">
        <svg width="22" height="34" viewBox="0 0 22 34" aria-hidden="true">
          <rect x="1.5" y="1.5" width="19" height="31" rx="3" fill="none" stroke="#fff" stroke-width="2.5"/>
          <circle cx="11" cy="28" r="1.6" fill="#fff"/>
        </svg>
        <span>1-888-VOLMI-15<br>317-555-0192</span>
      </div>
      <div class="contact-row">
        <svg width="24" height="18" viewBox="0 0 24 18" aria-hidden="true">
          <rect x="1" y="1" width="22" height="16" fill="none" stroke="#fff" stroke-width="2"/>
          <polyline points="1,1 12,10 23,1" fill="none" stroke="#fff" stroke-width="2"/>
        </svg>
        <span>info@volmihome.example</span>
      </div>
    </div>
  </div>
</section>

<section class="card card-back" aria-label="Business card back">
  <svg class="card-art" viewBox="0 0 720 411" preserveAspectRatio="none" aria-hidden="true">
    <line x1="0" y1="82" x2="720" y2="50" stroke="var(--line-red)" stroke-width="2"/>
    <line x1="0" y1="360" x2="720" y2="328" stroke="var(--line-red)" stroke-width="2"/>
  </svg>

  <p class="credentials">licensed . insured . bonded</p>

  <div class="company company-large">
    <span class="company-dot"></span>
    <span class="company-name">Volmi Home Remodeling</span>
  </div>

  <p class="website">www.volmihome.example</p>
</section>

</body>
</html>
```